Bref créative
Modern Business Name Card for IT Company
qLumio Sdn Bhd
Simple
Marissa Tanaka
Senior Manager
Lot C-17, 5B Floor,
8 Kilner Plaza,
No. 7, Jalan 24/6
47810 Petaling Jaya
Selangor, Malaysia
marissa@qlumiomarketing.example
www.qlumiomarketing.example
2187605-K
Kindly change the tagline of the website to a different font Segoe UI Semibold since the current font seem to rough and thick. Thanks.

```html
<!DOCTYPE html>
<html lang="en">
<head>
<meta charset="utf-8">
<title>qLumio Sdn Bhd – Business Card</title>
<link rel="stylesheet" href="https://fonts.googleapis.com/css2?family=Michroma&family=Open+Sans:wght@600&display=swap">
<style>
  :root {
    --bg: #e4e5e7;
    --card-white: #ffffff;
    --brand-blue: #1565c8;
    --deep-blue: #0a3a94;
    --sky-blue: #2f86dc;
    --leaf-green: #5fae2e;
    --text-grey: #6b6f76;
    --text-dark: #3c4048;
  }
  * { margin: 0; padding: 0; box-sizing: border-box; }
  html, body {
    width: 1200px; height: 987px; overflow: hidden;
    background: var(--bg);
  }
  .stage {
    width: 1200px; height: 987px;
    display: flex; flex-direction: column;
    align-items: center; justify-content: center; gap: 40px;
  }
  .card {
    position: relative;
    width: 760px; height: 434px;
    border-radius: 20px;
    overflow: hidden;
    box-shadow: 0 10px 28px rgba(0,0,0,0.18);
  }

  /* Back side */
  .card-back {
    background: radial-gradient(ellipse at 30% 25%, var(--sky-blue) 0%, var(--brand-blue) 45%, var(--deep-blue) 100%);
  }
  .card-back .website {
    position: absolute; right: 56px; bottom: 46px;
    font-family: "Michroma", sans-serif;
    font-size: 15px; letter-spacing: 4px;
    color: #ffffff; text-transform: uppercase;
  }

  /* Front side */
  .card-front { background: var(--card-white); }
  .swoosh { position: absolute; left: 0; top: 0; width: 760px; height: 434px; }

  .brand {
    position: absolute; top: 62px; left: 0; width: 100%;
    display: flex; align-items: center; justify-content: center; gap: 14px;
  }
  .brand-dot {
    width: 44px; height: 44px; border-radius: 50%;
    background: var(--brand-blue);
  }
  .brand-name {
    font-family: "Michroma", sans-serif;
    font-size: 50px; color: var(--brand-blue);
    letter-spacing: 2px;
  }

  .person {
    position: absolute; top: 150px; left: 0; width: 100%;
    text-align: center; font-family: "Michroma", sans-serif;
  }
  .person-name { font-size: 16px; color: var(--brand-blue); letter-spacing: 2px; text-transform: uppercase; }
  .person-title { margin-top: 6px; font-size: 11px; color: var(--text-grey); letter-spacing: 2px; text-transform: uppercase; }

  .details {
    position: absolute; top: 210px; left: 0; width: 100%;
    display: flex; justify-content: center;
    font-family: "Michroma", sans-serif;
    font-size: 10.5px; line-height: 18px; color: var(--text-dark);
    letter-spacing: 1px; text-transform: uppercase;
  }
  .address { text-align: right; padding-right: 16px; border-right: 1.5px solid var(--text-grey); }
  .contacts { padding-left: 16px; }
  .contacts li { list-style: none; display: flex; align-items: center; gap: 6px; }
  .contacts .email, .contacts .web { text-transform: lowercase; }
  .contacts .web { font-family: "Open Sans", sans-serif; font-weight: 600; font-size: 11px; letter-spacing: 0.6px; }
  .icon { width: 12px; height: 12px; flex: none; }
</style>
</head>
<body>
<main class="stage">

  <section class="card card-back" aria-label="Card back">
    <p class="website">www.qlumiomarketing.example</p>
  </section>

  <section class="card card-front" aria-label="Card front">
    <svg class="swoosh" viewBox="0 0 760 434" aria-hidden="true">
      <defs>
        <linearGradient id="blueSweep" x1="0" y1="0" x2="1" y2="1">
          <stop offset="0" stop-color="#2f86dc"/>
          <stop offset="1" stop-color="#0a3a94"/>
        </linearGradient>
        <linearGradient id="greenSweep" x1="0" y1="0" x2="1" y2="0">
          <stop offset="0" stop-color="#3f9a22"/>
          <stop offset="1" stop-color="#8cc63f"/>
        </linearGradient>
      </defs>
      <path d="M0,262 C170,300 380,400 760,428 L760,434 L0,434 Z" fill="url(#blueSweep)"/>
      <path d="M0,300 C190,330 400,408 700,434 L0,434 Z" fill="#ffffff"/>
      <path d="M0,312 C200,340 410,412 680,434 L0,434 Z" fill="url(#greenSweep)"/>
      <path d="M0,370 C120,385 240,410 360,434 L0,434 Z" fill="url(#blueSweep)"/>
    </svg>

    <div class="brand">
      <span class="brand-dot" aria-hidden="true"></span>
      <span class="brand-name">qLumio</span>
    </div>

    <div class="person">
      <p class="person-name">Marissa Tanaka</p>
      <p class="person-title">Senior Manager</p>
    </div>

    <div class="details">
      <address class="address" style="font-style:normal">
        Lot C-17, 5B Floor,<br>
        8 Kilner Plaza,<br>
        No. 7, Jalan 24/6<br>
        47810 Petaling Jaya<br>
        Selangor, Malaysia
      </address>
      <ul class="contacts">
        <li>
          <svg class="icon" viewBox="0 0 12 12" aria-hidden="true"><circle cx="6" cy="6" r="6" fill="#1565c8"/><path d="M4 3.2 L5 3 L5.6 4.6 L4.9 5.2 Q5.5 6.6 6.8 7.1 L7.4 6.4 L9 7 L8.8 8 Q6.5 8.6 4.7 6.8 Q3.2 5.2 4 3.2Z" fill="#fff"/></svg>
          603-5550 1492
        </li>
        <li class="email">
          <svg class="icon" viewBox="0 0 12 12" aria-hidden="true"><circle cx="6" cy="6" r="6" fill="#1565c8"/><rect x="3" y="4" width="6" height="4" fill="none" stroke="#fff" stroke-width="0.9"/><path d="M3 4 L6 6.3 L9 4" fill="none" stroke="#fff" stroke-width="0.9"/></svg>
          marissa@qlumiomarketing.example
        </li>
        <li class="web">
          <svg class="icon" viewBox="0 0 12 12" aria-hidden="true"><circle cx="6" cy="6" r="6" fill="#1565c8"/><circle cx="6" cy="6" r="3" fill="none" stroke="#fff" stroke-width="0.9"/><path d="M3 6 H9 M6 3 V9" stroke="#fff" stroke-width="0.7"/></svg>
          www.qlumiomarketing.example
        </li>
        <li>License # : 2187605-K</li>
      </ul>
    </div>
  </section>

</main>
</body>
</html>
```